Business Card for Brevel Coatings

We need a simple, yet out standing business card for our painting company.

Target Market(s)

wealthy; high-end neighborhoods, and businesses

Industry/Entity Type

Painting

Contact Information for Business Card

Name:
Doran Vask

Email:
d.vask@brevel-coatings.com

Website:
Brevel-coatings.com

Phone Number:
(555) 416-9073

Font styles to use
Serif
Sans Serif

Requirements
Must have
• slogan "Finishes Made Easy"
Should not have
• A title attached to the name on the card

```html
<!DOCTYPE html>
<html lang="en">
<head>
<meta charset="utf-8">
<title>Brevel Coatings – Business Card</title>
<link rel="stylesheet" href="https://fonts.googleapis.com/css2?family=Cinzel:wght@600;700&family=Open+Sans:wght@400;700&display=swap">
<style>
  :root {
    --page-bg: #ece9e4;
    --card-white: #ffffff;
    --green-dark: #233b16;
    --green-mid: #3f6a2c;
    --green-deep: #162a0d;
    --green-accent: #7fa83a;
    --rule-grey: #9aa394;
    --text-grey: #4a4f46;
  }
  * { margin: 0; padding: 0; box-sizing: border-box; }
  html, body { width: 1200px; height: 913px; overflow: hidden; }
  body { background: var(--page-bg); position: relative; }

  .card {
    position: absolute;
    width: 560px;
    height: 320px;
    border-radius: 18px;
    overflow: hidden;
    box-shadow: 0 10px 28px rgba(0,0,0,0.18);
  }

  /* Front */
  .card-front { left: 60px; top: 110px; background: var(--card-white); }
  .card-front .brand-name {
    position: absolute; right: 34px; top: 36px;
    font-family: "Cinzel", serif; font-weight: 700;
    font-size: 30px; color: var(--green-dark); letter-spacing: 1px;
  }
  .card-front .name-marker {
    position: absolute; left: 0; top: 122px;
    width: 18px; height: 18px; background: var(--green-accent);
  }
  .card-front .person-name {
    position: absolute; left: 30px; top: 118px;
    font-family: "Open Sans", sans-serif; font-weight: 700;
    font-size: 20px; line-height: 26px; color: var(--green-dark); letter-spacing: 0.5px;
  }
  .slogan-row {
    position: absolute; left: 30px; right: 0; top: 188px;
    display: flex; align-items: center; gap: 10px;
  }
  .slogan {
    font-family: "Cinzel", serif; font-weight: 700;
    font-size: 14px; line-height: 20px; color: var(--green-dark);
    letter-spacing: 0.5px; white-space: nowrap;
  }
  .slogan-rule { flex: 1; height: 1px; background: var(--rule-grey); }
  .contact-list {
    position: absolute; left: 30px; top: 228px;
    list-style: none;
    font-family: "Open Sans", sans-serif; font-size: 14px; color: var(--text-grey);
  }
  .contact-list li { display: flex; align-items: center; gap: 10px; line-height: 22px; }
  .contact-list svg { width: 12px; height: 12px; fill: var(--green-accent); flex: none; }

  /* Back */
  .card-back {
    left: 580px; top: 480px;
    background: linear-gradient(160deg, var(--green-mid) 0%, var(--green-dark) 55%, var(--green-deep) 100%);
  }
  .card-back .brand-name {
    position: absolute; right: 40px; top: 136px;
    font-family: "Cinzel", serif; font-weight: 700;
    font-size: 34px; color: var(--card-white); letter-spacing: 1px;
  }
</style>
</head>
<body>

<section class="card card-front" aria-label="Business card front">
  <div class="brand-name">Brevel Coatings</div>
  <div class="name-marker"></div>
  <h1 class="person-name">DORAN VASK</h1>
  <div class="slogan-row">
    <p class="slogan">FINISHES MADE EASY</p>
    <div class="slogan-rule"></div>
  </div>
  <ul class="contact-list">
    <li>
      <svg viewBox="0 0 12 12" aria-hidden="true"><path d="M2.5 0.8l2 2-1 1.4c.6 1.4 1.9 2.7 3.3 3.3l1.4-1 2 2-1.3 1.8C5 9.9 2.1 7 .7 2.1z"/></svg>
      (555) 416-9073
    </li>
    <li>
      <svg viewBox="0 0 12 12" aria-hidden="true"><path d="M0.5 2h11v8h-11z M1.5 3v.4l4.5 3 4.5-3V3z" fill-rule="evenodd"/></svg>
      d.vask@brevel-coatings.com
    </li>
    <li>
      <svg viewBox="0 0 12 12" aria-hidden="true"><circle cx="6" cy="6" r="5.5"/><path d="M0.5 6h11M6 .5c-2.5 3-2.5 8 0 11M6 .5c2.5 3 2.5 8 0 11" stroke="#fff" stroke-width="0.8" fill="none"/></svg>
      www.Brevel-coatings.com
    </li>
  </ul>
</section>

<section class="card card-back" aria-label="Business card back">
  <div class="brand-name">Brevel Coatings</div>
</section>

</body>
</html>
```